Flyer für Installationsfirma für hochwertige Multimedia- und Beschallungslösungen, insbesonder in Kirchen und öffentlichen Bereichen mit Menschenansammlungen
Zielgruppe
Wir sind eine Installationsfirma für hochwertige Multimedia- und Beschallungslösungen in akustisch schwierigen Räumen. Im weiteren auch der Umbau auf LED Leuchten und dazugehörende Steuerungen. Unser Geschäft ist in Festinstallationen und Rentalbereich 'unterteilt' Weitere Infos auch auf www. alpen-ton.ch
Unser Zielpublikum sind die Festinstallation für Kirchen und öffentliche Räume. Mehrzweckräume, Bühnen, Kirchen, Aulas, Bahnhofshallen, Warteräume, Konferenzräume, Tagungszentren usw. Bei diesem Flyer sollen speziell die Kirchen beworben werden. Es ist wichtig dass nebst den oben beschriebenen Leistungen auch die Displaylösung für Liedanzeigen hervorgehoben wird.
Aufgabenstellung
Ansprechender Werbe-Flyer A4 2 Seitig
Spezifische Bilder und Texte zu den versch. Angebotsbereichen für Kirchen im Anhang. Vorschläge des Grafikers sind willkommen !
Die Texte und Bilder sollten von uns angepasst und korrigiert werden können !

```html
<!DOCTYPE html>
<html lang="de">
<head>
<meta charset="utf-8">
<title>Alpenton – Audio &amp; Visual für Kirchen</title>
<link rel="stylesheet" href="https://fonts.googleapis.com/css2?family=Poppins:wght@600;800&family=Open+Sans:wght@400;700&display=swap">
<style>
  :root {
    --page-bg: #ececec;
    --navy-deep: #0d1422;
    --navy: #18243a;
    --footer-blue: #173a5e;
    --footer-blue-dark: #0f2a48;
    --accent: #2aa3dc;
    --white: #ffffff;
    --text-soft: #d5dbe4;
    --photo-warm: #8a6a45;
    --photo-dark: #3a2c20;
  }
  * { box-sizing: border-box; margin: 0; padding: 0; }
  html, body { width: 1200px; height: 800px; overflow: hidden; }
  body {
    background: var(--page-bg);
    display: flex; align-items: center; justify-content: center;
    font-family: "Open Sans", sans-serif;
  }
  .flyer {
    position: relative;
    width: 537px; height: 760px;
    background: var(--navy-deep);
    overflow: hidden;
    box-shadow: 0 12px 30px rgba(0,0,0,.25);
    color: var(--white);
  }
  .hero-photo {
    position: absolute; inset: 0 0 auto 0; height: 380px;
    background:
      linear-gradient(to bottom, rgba(13,20,34,0) 35%, rgba(24,36,58,.85) 75%, var(--navy-deep) 100%),
      radial-gradient(ellipse at 50% 35%, #c9a46a 0%, var(--photo-warm) 30%, var(--photo-dark) 75%);
  }
  .brand-badge {
    position: absolute; top: 56px; right: 34px;
    display: flex; align-items: center; gap: 8px;
  }
  .brand-badge .dot {
    width: 54px; height: 54px; border-radius: 50%;
    background: #3d5a9a; border: 3px solid var(--white);
  }
  .brand-badge .name {
    font-family: "Poppins", sans-serif; font-weight: 600;
    font-size: 15px; letter-spacing: 1px; color: var(--white);
  }
  .headline {
    position: absolute; top: 298px; left: 0; right: 0;
    text-align: center;
    font-family: "Poppins", sans-serif; font-weight: 800;
    font-size: 29px; line-height: 1.12; text-transform: uppercase;
  }
  .headline .accent { color: var(--accent); }
  .intro {
    position: absolute; top: 396px; left: 40px; right: 40px;
    text-align: center; font-size: 10.5px; line-height: 1.55;
    color: var(--text-soft);
  }
  .benefits {
    position: absolute; top: 500px; left: 38px;
    list-style: none;
  }
  .benefits li {
    display: flex; align-items: center; gap: 14px;
    font-weight: 700; font-size: 15px; height: 38px;
  }
  .benefits .marker {
    width: 10px; height: 10px; background: var(--accent);
  }
  .photo-frame {
    position: absolute; z-index: 2;
    width: 196px; height: 112px;
    border: 4px solid var(--white);
    box-shadow: 0 4px 10px rgba(0,0,0,.4);
  }
  .photo-altar {
    top: 484px; right: 28px;
    background: linear-gradient(135deg, #2a2420 0%, #8c7455 55%, #d8c7a4 100%);
  }
  .photo-speaker {
    top: 584px; right: 24px;
    background: linear-gradient(135deg, #6d5a3e 0%, #a48a62 50%, #cfc2a8 100%);
  }
  .footer-band {
    position: absolute; z-index: 1; left: 0; right: 0; bottom: 0; height: 84px;
    background: linear-gradient(90deg, var(--footer-blue) 0%, var(--footer-blue-dark) 100%);
    display: flex; align-items: center; gap: 26px; padding: 14px 30px 0;
  }
  .footer-band .wordmark {
    font-family: "Open Sans", sans-serif; font-weight: 400;
    font-size: 26px; letter-spacing: 3px; color: var(--white);
  }
  .footer-band .contact {
    font-size: 11px; font-weight: 700; line-height: 1.6;
  }
</style>
</head>
<body>
  <article class="flyer">
    <div class="hero-photo" role="img" aria-label="Foto: Innenraum einer gotischen Kirche mit Buntglasfenster und Altar"></div>

    <div class="brand-badge">
      <span class="dot"></span>
      <span class="name">ALPENTON</span>
    </div>

    <h1 class="headline">
      Benötigen Sie <span class="accent">Audio &amp;</span><br>
      <span class="accent">Visual</span> für Ihre Kirche?
    </h1>

    <p class="intro">
      Mit passenden, effizient eingesetzten Mitteln sorgen wir für Aufmerksamkeit bei Ihren
      Besucherinnen und Besuchern. Sie müssen sich um nichts kümmern. Anhand Ihrer Ideen
      und Budgetvorgaben entwickeln wir die optimalen Lösungen für Ihre Installation und
      liefern Ihnen den kompetenten Rundum-Service aus einer Hand.
    </p>

    <ul class="benefits">
      <li><span class="marker"></span>25 Jahre Erfahrung</li>
      <li><span class="marker"></span>Hochwertige Ausrüstung</li>
      <li><span class="marker"></span>Umfassender Service</li>
      <li><span class="marker"></span>engagiertes Team</li>
    </ul>

    <div class="photo-frame photo-altar" role="img" aria-label="Foto: Kirchenraum mit Altar, Kreuz und Lautsprecher im Vordergrund"></div>
    <div class="photo-frame photo-speaker" role="img" aria-label="Foto: Lautsprecher an der Kirchenwand neben Taufstein mit Blumen"></div>

    <footer class="footer-band">
      <span class="wordmark">ALPENTON</span>
      <div class="contact">
        Talstrasse 12 | 6400 Bergdorf | 041 555 12 34<br>
        mail@alpen-ton.ch | www.alpen-ton.ch
      </div>
    </footer>
  </article>
</body>
</html>
```